Catalogue Design Project

Hi Guys

We are a wine mail order company,
Enclosed is a detailed description of what we are after as well as examples from our competitors.

Feel free to be creative

Cheers

Dermot Whitby

Target market

- Middle aged wine drinkers of a rural background
- Gender, Male
- Occupation, Farmers

It Company

```html
<!DOCTYPE html>
<html lang="en">
<head>
<meta charset="utf-8">
<title>Redgum Valley Wines – Order Flyer</title>
<link href="https://fonts.googleapis.com/css2?family=Cinzel:wght@400;500&family=Crimson+Text:wght@400;700&family=Lato:wght@300;400&display=swap" rel="stylesheet">
<style>
  :root{
    --wine:#9b1c22;
    --wine-deep:#7e151a;
    --signal:#e0262b;
    --ink:#1b1b1b;
    --paper:#ffffff;
    --backdrop:#2b2b2b;
    --field-line:#9a9a9a;
    --field-text:#6b6b6b;
    --envelope:#dcdcdc;
  }
  *{box-sizing:border-box;margin:0;padding:0}
  html,body{width:1200px;height:1000px;overflow:hidden;background:var(--backdrop)}
  .canvas{position:relative;width:1200px;height:1000px}
  .flyer{position:absolute;left:244px;top:26px;width:714px;height:950px;background:var(--paper)}
  .abs{position:absolute}

  .top-rule{left:96px;top:50px;width:522px;height:10px}

  .headline{left:48px;top:70px;font-family:"Cinzel",serif;line-height:1;letter-spacing:3px}
  .headline .line{display:block;white-space:nowrap}
  .headline .free{color:var(--wine);font-size:37px}
  .headline .pay{color:var(--ink);font-size:31px;margin-top:3px}
  .headline .save{color:var(--wine);font-size:44px;margin-top:2px;letter-spacing:6px}

  .seal{width:120px;height:120px}
  .seal-award{left:66px;top:186px}
  .seal-guarantee{left:206px;top:186px}

  .case-contents{left:382px;top:76px;width:286px;height:244px}

  .offer-band{left:0;top:324px;width:714px;height:60px;background:var(--wine);color:#fff;text-align:center;font-family:"Cinzel",serif;border-top:1px dashed rgba(255,255,255,.35);border-bottom:1px dashed rgba(255,255,255,.35)}
  .offer-band .title{font-size:17px;letter-spacing:1px;margin-top:10px;line-height:20px}
  .offer-band .contact{font-size:16px;letter-spacing:.5px;line-height:20px}

  .section-label{font-family:"Crimson Text",serif;font-weight:700;font-size:13px;color:var(--ink)}
  .field{height:14px;border:1px solid var(--field-line);font-family:"Lato",sans-serif;font-weight:300;font-size:8px;color:var(--field-text);line-height:12px;padding-left:5px;text-transform:uppercase;white-space:nowrap}
  .check{font-family:"Lato",sans-serif;font-weight:300;font-size:8px;color:var(--field-text);display:flex;align-items:center;gap:9px;height:16px;white-space:nowrap}
  .check .box{width:16px;height:16px;border:1px solid var(--ink)}

  .cut-line{left:0;top:576px;width:714px;border-top:1px dashed var(--signal)}

  .envelope{left:41px;top:589px;width:630px;height:325px;background:linear-gradient(135deg,#f2f2f2 0%,var(--envelope) 60%,#c9c9c9 100%);box-shadow:6px 8px 10px rgba(0,0,0,.35)}
  .envelope .ribbon{left:0;top:0;width:180px;height:150px}
  .postage-note{right:16px;top:10px;font-family:"Lato",sans-serif;font-size:6.5px;color:#555;text-align:right;line-height:8px}
  .window{left:50px;top:168px;width:272px;height:82px;border:1px solid #b5b5b5;border-radius:6px;background:linear-gradient(180deg,#fafafa,#e6e6e6)}
  .address{left:18px;top:20px;font-family:"Crimson Text",serif;font-weight:700;font-size:14.5px;line-height:19px;color:var(--ink)}
</style>
</head>
<body>
<div class="canvas">
  <main class="flyer">

    <svg class="abs top-rule" viewBox="0 0 522 10" aria-hidden="true">
      <line x1="0" y1="5" x2="190" y2="5" stroke="#c33" stroke-width="1.5" stroke-dasharray="1.5 3"/>
      <line x1="332" y1="5" x2="522" y2="5" stroke="#c33" stroke-width="1.5" stroke-dasharray="1.5 3"/>
      <rect x="196" y="0" width="130" height="10" rx="4" fill="var(--signal)"/>
    </svg>

    <h1 class="abs headline">
      <span class="line free">FREE DELIVERY</span>
      <span class="line pay">PAY JUST $139.99</span>
      <span class="line save">SAVE $79.34</span>
    </h1>

    <svg class="abs seal seal-award" viewBox="0 0 120 120" role="img" aria-label="Red wax seal badge for award quality">
      <circle cx="60" cy="60" r="56" fill="var(--wine)"/>
    </svg>
    <svg class="abs seal seal-guarantee" viewBox="0 0 120 120" role="img" aria-label="Red wax seal badge for satisfaction guarantee">
      <circle cx="60" cy="60" r="56" fill="var(--wine)"/>
    </svg>

    <div class="abs case-contents" role="img" aria-label="Case contents: a row of twelve red wine bottles beneath a red ribbon banner" style="background:linear-gradient(180deg,var(--wine) 0%,var(--wine) 30%,#3a1a1e 55%,#2a1a1c 100%)"></div>

    <section class="abs offer-band">
      <p class="title">STRICTLY LIMITED OFFER - ORDER NOW</p>
      <p class="contact">CALL 1300 48 21 57, RETURN PAYMENT SLIP TO US, OR FAX (02) 9555 0142</p>
    </section>

    <form class="order-form">
      <p class="abs section-label" style="left:46px;top:398px">Your Delivery Details</p>
      <div class="abs field" style="left:193px;top:400px;width:85px">Title</div>
      <div class="abs field" style="left:285px;top:400px;width:178px">First Name</div>
      <div class="abs field" style="left:470px;top:400px;width:176px">Last Name</div>

      <div class="abs field" style="left:47px;top:421px;width:115px">Street No.</div>
      <div class="abs field" style="left:171px;top:421px;width:352px">Street Name</div>
      <div class="abs field" style="left:532px;top:421px;width:114px">Postcode</div>

      <div class="abs field" style="left:47px;top:446px;width:148px">City</div>
      <div class="abs field" style="left:203px;top:446px;width:90px">State</div>
      <div class="abs field" style="left:302px;top:446px;width:164px">Primary Phone</div>
      <div class="abs field" style="left:475px;top:446px;width:171px">Mobile Phone</div>

      <p class="abs section-label" style="left:46px;top:472px">Your Payment Details</p>
      <div class="abs field" style="left:47px;top:494px;width:115px">Card Type</div>
      <div class="abs field" style="left:171px;top:494px;width:351px">Card No.</div>
      <div class="abs field" style="left:531px;top:494px;width:115px">Expiry</div>

      <div class="abs field" style="left:47px;top:518px;width:246px">Name on Card</div>
      <div class="abs field" style="left:302px;top:518px;width:169px">Signature</div>
      <div class="abs field" style="left:477px;top:518px;width:169px">Date</div>

      <div class="abs check" style="left:47px;top:541px"><span class="box"></span>I acknowledge that i am 18 years or over</div>
      <div class="abs check" style="left:231px;top:541px"><span class="box"></span>I have enclosed a check to “Redgum Valley Wines”</div>
    </form>

    <div class="abs cut-line"></div>

    <section class="abs envelope">
      <svg class="abs ribbon" viewBox="0 0 180 150" aria-hidden="true">
        <polygon points="0,112 0,136 172,0 148,0" fill="var(--wine)"/>
      </svg>
      <p class="abs postage-note">No postage stamp required<br>if posted in Australia</p>
      <div class="abs window">
        <address class="abs address" style="font-style:normal">
          Redgum Valley Wines<br>
          14 Fenwick Street<br>
          BELLBROOK, NSW, 2440
        </address>
      </div>
    </section>

  </main>
</div>
</body>
</html>
```